Designing a cover for my upcoming book.

A brief description of the theme which the book cover design has to capture is given below:
The title and sub-title of the book are as follows:
Title : Adrift Among Quiet Harbours
Sub-Title: Coastal Fisheries of the Lowlands - 3
The book is a critical examination of the laws which govern the conservation of wildlife in India. It describes how contradictory provisions within and between various laws make conservation of the same wildlife difficult which these laws are together meant to preserve. The book primarily discusses five laws which have a bearing on the subject, namely:
The Indian Forest Act, 1927;
The Wild Life (Protection) Act, 1972;
Forest (Conservation) Act, 1980
Biological Diversity Act, 2002; and
The Forest Rights Act, 2006.
Out of these five laws, the Wild Life (Protection) Act has been specifically mandated to protect wildlife. The primary objectives of other laws are different (as their names indicate) but all have a bearing on the conservation of wild animals as well. However all these laws have some contradictory provisions so that if the authorities comply with one law, they violate some other law. The same problem exists within the Wild Life (Protection) Act also. Many of its provisions can be enforced only by ignoring or violating others. As a result the authorities cannot devise a clear road map for conservation. Thus, conservation of wildlife in India is a victim of its own laws.
The book cover must illustrate this paradox. Perhaps the designer can create a tangle/web of these titles, running/cutting across each other, with one or more of charismatic Indian animals (e.g. tigers, elephants, leopards, spotted deer etc.) entangled in this mesh. The fonts and colours of the text (titles) can be artistically and creatively designed. If possible, the animal(s) should look a bit confused or perplexed. We can also show a ranger looking at this tangle in a helpless or confused manner (say raised hands thrown up).
This is only a suggestion. If the artist thinks he can depict the theme better in some other way, I will be happy to look at it.

Target Market(s)

Environmentalists, foresters, wildlife enthusiasts and conservationists, policy makers, advocates, environmental activists, lawyers, training institutes.

Requirements
Must have
• A beautiful picture of a tiger or some other Indian wild animal(s). Also, a net consisting of the names of the laws mentioned in the brief.
Nice to have
• The image of a ranger who looks a bit helpless and hassled. Perhaps in the background.

```html
<!DOCTYPE html>
<html lang="en">
<head>
<meta charset="utf-8">
<title>Adrift Among Quiet Harbours – Cover</title>
<link rel="stylesheet" href="https://fonts.googleapis.com/css2?family=Cormorant+SC:wght@600;700&family=Crimson+Text:wght@400;600&family=Roboto+Condensed:wght@700&display=swap">
<style>
  :root {
    --parchment-light: #f1e4c4;
    --parchment-mid: #e2cd9d;
    --parchment-dark: #c9a96c;
    --ink: #2a1d12;
    --ink-soft: #3b2a1a;
    --title-red: #7a1414;
    --title-black: #0f0a06;
    --subtitle-brown: #3a1d10;
    --paper-white: #ffffff;
    --photo-haze: #d8bd86;
    --photo-amber: #a9803f;
    --photo-deep: #5a3d1c;
  }
  * { box-sizing: border-box; margin: 0; padding: 0; }
  html, body { width: 1200px; height: 831px; overflow: hidden; background: #ffffff; }
  .cover {
    position: relative; width: 1200px; height: 831px; overflow: hidden;
    background: radial-gradient(ellipse at 40% 40%, var(--parchment-light) 0%, var(--parchment-mid) 60%, var(--parchment-dark) 100%);
    color: var(--ink);
  }

  /* Back cover */
  .back { position: absolute; left: 0; top: 0; width: 560px; height: 831px; }
  .series {
    font-family: "Roboto Condensed", sans-serif; font-weight: 700;
    color: var(--subtitle-brown); text-transform: uppercase; letter-spacing: -0.3px;
  }
  .back .series { position: absolute; top: 25px; left: 0; width: 566px; text-align: center; font-size: 22px; }
  .back-title {
    position: absolute; top: 52px; left: 0; width: 566px; text-align: center;
    font-family: "Cormorant SC", serif; font-weight: 700; color: var(--title-red);
    font-size: 47px; line-height: 48px; letter-spacing: 1px;
  }
  .blurb {
    position: absolute; top: 162px; left: 24px; width: 514px;
    font-family: "Crimson Text", serif; font-size: 14px; line-height: 20px; color: var(--ink-soft);
    text-align: justify;
  }
  .blurb ul { list-style: none; }
  .blurb li::before { content: "●"; font-size: 10px; margin-right: 6px; position: relative; top: -1px; }
  .author-photo {
    position: absolute; top: 529px; left: 25px; width: 79px; height: 110px;
    background: var(--paper-white); border: 1.5px solid var(--title-black);
  }
  .bio {
    position: absolute; top: 524px; left: 110px; width: 428px;
    font-family: "Crimson Text", serif; font-size: 14px; line-height: 20px; color: var(--ink-soft); text-align: justify;
  }
  .bio-tail {
    position: absolute; top: 648px; left: 24px; width: 514px;
    font-family: "Crimson Text", serif; font-size: 14px; line-height: 20px; color: var(--ink-soft);
  }
  .crowd-scene {
    position: absolute; left: 40px; bottom: 0; width: 300px; height: 150px;
    background: linear-gradient(to top, rgba(90,61,28,0.55), rgba(90,61,28,0.25) 60%, rgba(90,61,28,0));
  }
  .publisher {
    position: absolute; left: 22px; top: 742px; display: flex; align-items: center; gap: 6px;
    font-family: "Roboto Condensed", sans-serif; font-weight: 700; font-size: 13px; color: var(--paper-white);
    text-transform: uppercase;
  }
  .publisher-dot { width: 14px; height: 14px; border-radius: 50%; background: var(--paper-white); }

  /* Spine */
  .spine { position: absolute; left: 566px; top: 0; width: 76px; height: 831px; border-left: 1px solid rgba(120,90,50,0.25); border-right: 1px solid rgba(120,90,50,0.25); }
  .spine-title {
    position: absolute; top: 50px; left: 50%; transform: translateX(-50%); writing-mode: vertical-rl;
    font-family: "Cormorant SC", serif; font-weight: 700; font-size: 30px; color: var(--title-black); white-space: nowrap;
  }
  .spine-author {
    position: absolute; top: 625px; left: 50%; transform: translateX(-50%); writing-mode: vertical-rl;
    font-family: "Roboto Condensed", sans-serif; font-weight: 700; font-size: 26px; color: var(--title-black); white-space: nowrap;
  }

  /* Front cover */
  .front { position: absolute; left: 642px; top: 0; width: 558px; height: 831px; }
  .front-scene {
    position: absolute; inset: 0;
    background:
      radial-gradient(ellipse at 50% 62%, var(--photo-deep) 0%, rgba(90,61,28,0.6) 25%, rgba(90,61,28,0) 50%),
      linear-gradient(to bottom, var(--parchment-light) 0%, var(--photo-haze) 40%, var(--photo-amber) 75%, var(--photo-deep) 100%);
  }
  .front .series { position: absolute; top: 26px; left: 0; width: 100%; text-align: center; font-size: 24px; }
  .front-title {
    position: absolute; top: 100px; left: 0; width: 100%; text-align: center;
    font-family: "Cormorant SC", serif; font-weight: 700; color: var(--title-black); text-transform: uppercase;
  }
  .front-title .line-1 { display: block; font-size: 92px; line-height: 88px; }
  .front-title .line-2 { display: block; font-size: 54px; line-height: 56px; }
  .front-title .line-3 { display: block; font-size: 84px; line-height: 92px; }
  .front-author {
    position: absolute; top: 770px; left: 20px;
    font-family: "Roboto Condensed", sans-serif; font-weight: 700; font-size: 40px; color: var(--paper-white);
  }
</style>
</head>
<body>
<main class="cover">

  <section class="back">
    <p class="series">Coastal Fisheries of the Lowlands-3</p>
    <h2 class="back-title">Adrift Among<br>Quiet Harbours</h2>
    <div class="blurb">
      <p>The book is a critical examination of the laws which govern the conservation of wildlife in India.</p>
      <p>It describes how contradictory provisions within and between various laws make conservation of the same wildlife difficult which these laws are together meant to preserve. The book primarily discusses five laws which have a bearing on the subject, namely:</p>
      <ul>
        <li>The Indian Forest Act, 1927;</li>
        <li>The Wild Life (Protection) Act, 1972;</li>
        <li>Forest (Conservation) Act, 1980</li>
        <li>Biological Diversity Act, 2002; and</li>
        <li>The Forest Rights Act, 2006.</li>
      </ul>
      <p>Out of these five laws, the Wild Life (Protection) Act has been specifically mandated to protect wildlife. The primary objectives of other laws are different (as their names indicate) but all have a bearing on the conservation of wild animals as well. However all these laws have some contradictory provisions so that if the authorities comply with one law, they violate some other law. The same problem exists within the Wild Life (Protection) Act also. Many of its provisions can be enforced only by ignoring or violating others. As a result the authorities cannot devise a clear road map for conservation. Thus, conservation of wildlife in India is a victim of its own laws.</p>
    </div>
    <div class="author-photo" role="img" aria-label="Author portrait placeholder"></div>
    <p class="bio">Lorem Ipsum is simply dummy text of the printing and typesetting industry. Lorem Ipsum has been the industry's standard dummy text ever since the 1500s, when an unknown printer took a galley of type and scrambled it to make a type specimen book. It has survived not only five centuries, but also the leap into electronic typesetting, remaining essentially unchanged. It was popularised in the 1960s with the release of Letraset sheets containing</p>
    <p class="bio-tail">Lorem Ipsum is simply dummy text of the printing and typesetting industry. Lorem Ipsum has been the industry's standard dummy text essentially Lorem Ipsum.</p>
    <div class="crowd-scene" role="img" aria-label="Faded silhouettes of protesters holding banners"></div>
    <div class="publisher"><span class="publisher-dot"></span><span>Tidewell Press</span></div>
  </section>

  <section class="spine">
    <p class="spine-title">Adrift Among Quiet Harbours</p>
    <p class="spine-author">RK VARDEN</p>
  </section>

  <section class="front">
    <div class="front-scene" role="img" aria-label="Sepia photograph of an elephant walking through a misty forest, with a domed court building in the background"></div>
    <p class="series">Coastal Fisheries of the Lowlands-3</p>
    <h1 class="front-title">
      <span class="line-1">Adrift</span>
      <span class="line-2">Among Quiet</span>
      <span class="line-3">Harbours</span>
    </h1>
    <p class="front-author">RK VARDEN</p>
  </section>

</main>
</body>
</html>
```